Vitamin Business Needs a Label Design

Hello. We are high-quality/healthy vitamin/supplement company, and we are in need of a Label design for a vitamin bottle.
Bottle will be either white or brown color. Label size will be 74mm*220mm. Please pick one logo from the attachments(you may use new design for the logo if you'd like to). On the front, please put two icon graphics(like certified organic sticker on food products) for "Kosher Certified" and "Vegetable Capsules". I attached sample of icon for your reference. I'm attaching files for the information. I will also put some example label designs on the brief page. Please let me know if you have any question. Thank you so much for the works!

Industry/Entity Type

Business

Font styles to use
Serif
Sans Serif

Requirements
Must have
• Information on the files. I may put barcode later, so if possible, please leave a space for barcode. Thank you.
Nice to have
• White or Ivory color for the label background would be nice. But you may use different color if you'd like to. For your information, I prefer logo 2 over logo 1, but you can use any logo as long as the design looks great.
Should not have
• Please do not use sample icon or use icon from online. It is because there may be copyright issues. For color, please do not use dark colors for label background color. (if it looks very good, then its okay).

```html
<!DOCTYPE html>
<html lang="en">
<head>
<meta charset="utf-8">
<title>Verdamin Multivitamin Label</title>
<link rel="stylesheet" href="https://fonts.googleapis.com/css2?family=Audiowide&family=Raleway:wght@300;700&display=swap">
<style>
  :root {
    --page: #ffffff;
    --band-light: #e9e9e9;
    --band-mid: #bdbdbd;
    --brand-ink: #3a3a3a;
    --leaf: #6aad45;
    --lime: #74c53a;
    --grass: #2bb04c;
    --forest: #238a3e;
    --teal: #1fa27a;
    --deep-teal: #1a7d5e;
    --ink-dark: #1f2a22;
    --ink-light: #f2f7f0;
  }
  html, body {
    margin: 0;
    width: 1200px;
    height: 1200px;
    overflow: hidden;
    background: var(--page);
  }
  .label {
    position: absolute;
    left: 100px;
    top: 180px;
    width: 1000px;
    height: 840px;
  }
  .label-facets {
    position: absolute;
    inset: 0;
  }
  .brand-band {
    position: absolute;
    left: 0;
    top: 0;
    width: 149px;
    height: 840px;
    box-sizing: border-box;
    padding: 0 0 70px 10px;
    display: flex;
    align-items: flex-end;
    gap: 8px;
    overflow: hidden;
    background: linear-gradient(90deg, var(--band-mid), var(--band-light) 55%, #d6d6d6);
  }
  .brand-name {
    writing-mode: vertical-rl;
    transform: rotate(180deg);
    font-family: "Raleway", sans-serif;
    font-weight: 300;
    font-size: 106px;
    line-height: 0.9;
    color: var(--brand-ink);
    white-space: nowrap;
  }
  .brand-sub {
    writing-mode: vertical-rl;
    transform: rotate(180deg);
    height: 460px;
    text-align: end;
    font-family: "Raleway", sans-serif;
    font-weight: 700;
    font-size: 9px;
    line-height: 1.35;
    letter-spacing: 0.5px;
    text-transform: uppercase;
    color: var(--brand-ink);
    white-space: nowrap;
  }
  .headline {
    position: absolute;
    left: 373px;
    top: 110px;
    font-family: "Audiowide", sans-serif;
    text-transform: uppercase;
    transform: skewX(-8deg);
  }
  .headline .kind {
    font-size: 38px;
    color: var(--ink-dark);
    line-height: 1;
  }
  .headline .count {
    font-size: 56px;
    color: var(--ink-light);
    line-height: 1.1;
  }
  .badge-kosher {
    position: absolute;
    left: 468px;
    top: 240px;
    width: 104px;
    height: 104px;
    border-radius: 50%;
    background: var(--ink-dark);
  }
  .badge-veg {
    position: absolute;
    left: 675px;
    top: 256px;
    width: 170px;
    height: 72px;
    border-radius: 36px;
    background: var(--ink-light);
  }
  .support-title {
    position: absolute;
    left: 373px;
    top: 425px;
    font-family: "Audiowide", sans-serif;
    font-size: 36px;
    text-transform: uppercase;
    color: var(--ink-light);
    transform: skewX(-8deg);
  }
  .benefit {
    position: absolute;
    left: 149px;
    height: 56px;
    display: flex;
    align-items: center;
  }
  .benefit .rule {
    width: 176px;
    height: 4px;
    background: var(--ink-light);
  }
  .benefit .icon {
    width: 52px;
    height: 52px;
    flex: none;
  }
  .benefit .text {
    margin-left: 22px;
    font-family: "Audiowide", sans-serif;
    font-size: 50px;
    text-transform: uppercase;
    color: var(--ink-light);
    white-space: nowrap;
    transform: skewX(-8deg);
  }
</style>
</head>
<body>
  <div class="label">
    <svg class="label-facets" viewBox="0 0 1000 840" width="1000" height="840" aria-hidden="true">
      <rect x="149" y="0" width="851" height="840" fill="var(--leaf)"/>
      <polygon points="500,0 1000,0 1000,500 620,260" fill="var(--lime)"/>
      <polygon points="620,260 1000,0 1000,840" fill="var(--grass)"/>
      <polygon points="860,0 1000,0 1000,840 800,150" fill="var(--forest)" opacity="0.55"/>
      <polygon points="149,840 149,720 620,260 1000,840" fill="var(--teal)"/>
      <polygon points="620,260 1000,840 820,840 700,560" fill="var(--deep-teal)" opacity="0.7"/>
    </svg>

    <div class="brand-band">
      <div class="brand-name">Verdamin</div>
      <div class="brand-sub">Multivitamin/Multimineral<br>Supplement</div>
    </div>

    <div class="headline">
      <div class="kind">Dietary Supplement</div>
      <div class="count">180 Capsules</div>
    </div>

    <div class="badge-kosher"></div>
    <div class="badge-veg"></div>

    <div class="support-title">Essential support for:</div>

    <div class="benefit" style="top:486px">
      <span class="rule"></span>
      <svg class="icon" viewBox="0 0 52 52" aria-hidden="true">
        <circle cx="26" cy="26" r="22" fill="none" stroke="var(--ink-light)" stroke-width="4"/>
        <circle cx="19" cy="21" r="3" fill="var(--ink-light)"/>
        <circle cx="33" cy="21" r="3" fill="var(--ink-light)"/>
        <path d="M16 30 Q26 40 36 30" fill="none" stroke="var(--ink-light)" stroke-width="3.5" stroke-linecap="round"/>
      </svg>
      <span class="text">Overall Health</span>
    </div>

    <div class="benefit" style="top:563px">
      <span class="rule"></span>
      <svg class="icon" viewBox="0 0 52 52" aria-hidden="true">
        <circle cx="26" cy="26" r="22" fill="none" stroke="var(--ink-light)" stroke-width="4"/>
        <path d="M16 17 L26 13 L36 17 L36 27 Q36 35 26 40 Q16 35 16 27 Z" fill="none" stroke="var(--ink-light)" stroke-width="3"/>
        <path d="M26 31 L21 26 Q20 22 23 22 Q25 22 26 24 Q27 22 29 22 Q32 22 31 26 Z" fill="var(--ink-light)"/>
      </svg>
      <span class="text">Immune System</span>
    </div>

    <div class="benefit" style="top:646px">
      <span class="rule"></span>
      <svg class="icon" viewBox="0 0 52 52" aria-hidden="true">
        <circle cx="26" cy="26" r="22" fill="none" stroke="var(--ink-light)" stroke-width="4"/>
        <polygon points="29,11 18,28 26,28 22,42 35,23 27,23" fill="var(--ink-light)"/>
      </svg>
      <span class="text">Energy</span>
    </div>

    <div class="benefit" style="top:731px">
      <span class="rule"></span>
      <svg class="icon" viewBox="0 0 52 52" aria-hidden="true">
        <circle cx="26" cy="26" r="22" fill="none" stroke="var(--ink-light)" stroke-width="4"/>
        <circle cx="26" cy="17" r="6" fill="var(--ink-light)"/>
        <circle cx="17" cy="32" r="6" fill="var(--ink-light)"/>
        <circle cx="35" cy="32" r="6" fill="var(--ink-light)"/>
        <circle cx="26" cy="27" r="3" fill="var(--teal)"/>
      </svg>
      <span class="text">Metabolism</span>
    </div>
  </div>
</body>
</html>
```